Ridgeport Clay Range Facebook Design Project

I want a Facebook design based on my attached logo. I would like it to be classy, colorful, unusual.

Font:
- Serpentine-Bold-Bold for "RIDGEPORT"
- BrowalliaUPC for "CLAY RANGE"

Colors (CMYK code):
- BLACK ....... 0; 0; 0; 100;
- ORANGE ... gradient from 0; 65; 97.5; 0 to 0; 39; 97.5; 0

```html
<!DOCTYPE html>
<html lang="en">
<head>
<meta charset="utf-8">
<title>Ridgeport Clay Range – Cover</title>
<link href="https://fonts.googleapis.com/css2?family=Russo+One&family=Arimo:wght@400&display=swap" rel="stylesheet">
<style>
  :root {
    --orange-light: #f9a733;
    --orange-deep: #f0762e;
    --orange-glow: rgba(255, 196, 110, 0.45);
    --black: #000000;
    --white: #ffffff;
  }
  html, body {
    margin: 0;
    padding: 0;
    overflow: hidden;
    background: var(--white);
  }
  .cover {
    position: relative;
    width: 1200px;
    height: 444px;
    overflow: hidden;
    background: linear-gradient(180deg, var(--orange-light) 0%, var(--orange-deep) 100%);
  }
  .texture {
    position: absolute;
    left: 96px;
    top: 96px;
    width: 630px;
    height: 348px;
    background: radial-gradient(ellipse at 50% 50%, var(--orange-glow) 0%, rgba(255, 196, 110, 0) 70%);
  }
  .brand-mark {
    position: absolute;
    left: 0;
    top: 0;
    width: 1200px;
    height: 444px;
  }
  .brand-mark__square {
    position: absolute;
    left: 812px;
    top: -20px;
    width: 330px;
    height: 330px;
    background: var(--black);
  }
  .brand-mark__name {
    position: absolute;
    right: 40px;
    top: 346px;
    font-family: "Arimo", sans-serif;
    font-weight: 400;
    font-size: 46px;
    line-height: 1;
    color: var(--black);
    white-space: nowrap;
  }
  .headline {
    position: absolute;
    left: 48px;
    top: 38px;
    margin: 0;
    font-family: "Russo One", sans-serif;
    font-size: 132px;
    line-height: 1;
    letter-spacing: 2px;
    color: var(--black);
    transform: scaleX(1.3);
    transform-origin: left top;
    white-space: nowrap;
    text-shadow:
      2px 0 0 var(--white), -2px 0 0 var(--white),
      0 2px 0 var(--white), 0 -2px 0 var(--white),
      2px 2px 0 var(--white), -2px -2px 0 var(--white),
      2px -2px 0 var(--white), -2px 2px 0 var(--white);
  }
  .subline {
    position: absolute;
    left: 54px;
    top: 178px;
    margin: 0;
    font-family: "Arimo", sans-serif;
    font-weight: 400;
    font-size: 68px;
    line-height: 1;
    color: var(--white);
    white-space: nowrap;
  }
</style>
</head>
<body>
  <div class="cover">
    <div class="texture" role="img" aria-label="Faint outlined lettering pattern in light orange"></div>
    <div class="brand-mark">
      <div class="brand-mark__square"></div>
      <div class="brand-mark__name">Ridgeport Clay Range</div>
    </div>
    <h1 class="headline">RIDGEPORT</h1>
    <p class="subline">CLAY RANGE</p>
  </div>
</body>
</html>
```